Need Business Card for our Real Estate Business with Sales Executive's Picture

PANTONE 484 C ( RED)

PANTONE 2766 C ( BLUE

Industry/Entity Type

Real Estate

Contact Information for Business Card

Name, Mobile, email, & picture of Person
Agency Phone, address, Web address

Requirements
Must have
• Our Logo Colours, Agent Picture,

```html
<!DOCTYPE html>
<html lang="en">
<head>
<meta charset="utf-8">
<title>Dunecrest Realty – Business Card</title>
<link rel="stylesheet" href="https://fonts.googleapis.com/css2?family=EB+Garamond:wght@400;500;700&display=swap">
<style>
  :root {
    --navy: #141b4d;
    --brand-red: #8f2a22;
    --ink: #1d1d22;
    --card-cream: #f1f0ea;
    --card-cream-edge: #e3e3dc;
    --backdrop: #e8e6e1;
    --white: #ffffff;
  }
  * { box-sizing: border-box; margin: 0; padding: 0; }
  html, body {
    width: 1200px; height: 800px; overflow: hidden;
    background: var(--backdrop);
    font-family: "EB Garamond", Georgia, serif;
  }
  .canvas {
    position: relative; width: 1200px; height: 800px;
    display: flex; align-items: center; justify-content: center; gap: 48px;
  }
  .card {
    width: 500px; height: 286px; position: relative; overflow: hidden;
    box-shadow: 0 6px 18px rgba(0,0,0,0.18);
  }
  /* Back side */
  .card-back {
    background: var(--navy);
    display: flex; align-items: center; justify-content: center;
  }
  .brand-lockup {
    display: flex; align-items: center; gap: 14px;
  }
  .brand-square {
    width: 14px; height: 14px; background: var(--white);
  }
  .brand-name {
    color: var(--white); font-weight: 500; font-size: 38px;
    letter-spacing: 0.08em; line-height: 1;
  }
  /* Front side */
  .card-front {
    background: linear-gradient(120deg, var(--card-cream) 0%, var(--card-cream-edge) 100%);
  }
  .agent-photo {
    position: absolute; left: 0; top: 0; width: 200px; height: 286px;
    background: linear-gradient(180deg, #ececea 0%, #dcdcdc 35%, #2c3f86 60%, #1e2d6b 100%);
  }
  .agent-details {
    position: absolute; left: 222px; top: 36px; right: 18px; color: var(--ink);
  }
  .agent-name {
    color: var(--brand-red); font-weight: 700; font-size: 24px;
    letter-spacing: 0.02em; line-height: 1;
  }
  .agent-title { font-size: 16px; margin-top: 2px; }
  .office-address { font-size: 15px; line-height: 1.2; margin-top: 28px; }
  .contact-list { list-style: none; margin-top: 14px; font-size: 15px; }
  .contact-list li { display: flex; align-items: center; gap: 10px; line-height: 1.3; }
  .contact-list svg { width: 14px; height: 14px; flex: none; fill: none; stroke: var(--brand-red); stroke-width: 1.8; }
  .contact-list .no-icon { padding-left: 24px; }
</style>
</head>
<body>
<main class="canvas">
  <section class="card card-back" aria-label="Card back">
    <div class="brand-lockup">
      <span class="brand-square"></span>
      <span class="brand-name">DUNECREST REALTY</span>
    </div>
  </section>

  <section class="card card-front" aria-label="Card front">
    <div class="agent-photo" role="img" aria-label="Portrait of the sales executive in a navy suit against a light wall"></div>
    <div class="agent-details">
      <h1 class="agent-name">MARCUS HALE</h1>
      <p class="agent-title">Sales Executive</p>
      <p class="office-address">418 Willowmere<br>Avenue Ashford, MA 01842</p>
      <ul class="contact-list">
        <li>
          <svg viewBox="0 0 14 14"><rect x="3.5" y="1" width="7" height="12" rx="1"/><line x1="6" y1="11" x2="8" y2="11"/></svg>
          555-204-1188
        </li>
        <li>
          <svg viewBox="0 0 14 14"><path d="M3 1.5l2.5 3-1.5 1.5c.8 1.8 2.2 3.2 4 4l1.5-1.5 3 2.5-1.5 1.5C6 12.5 1.5 8 1.5 3z"/></svg>
          555-307-2264
        </li>
        <li>
          <svg viewBox="0 0 14 14"><rect x="1" y="3" width="12" height="8"/><polyline points="1,3 7,8 13,3"/></svg>
          hello@DunecrestRealty.com
        </li>
        <li>
          <svg viewBox="0 0 14 14"><circle cx="7" cy="7" r="5.8"/><ellipse cx="7" cy="7" rx="2.5" ry="5.8"/><line x1="1.2" y1="7" x2="12.8" y2="7"/></svg>
          www.DunecrestRealty.com
        </li>
      </ul>
    </div>
  </section>
</main>
</body>
</html>
```